Real Estate Company Looking for Business Card Designs for 3 Executives

Hello!
Thanks so much for considering our project! We are a real estate investment company located in Edmonton, Alberta called Marlbeck Group of Companies. We invest/develop both commercial and residential real estate and are looking to create 3 DOUBLE-SIDED business cards for 3 top executives in the company! (for some reason it won't let us select the double-sided option, but yes, the cards are double sided and would be happy to tip extra)

We have certain guidelines that we want our business cards to for sure follow - the back of the Business card has to be the Black Background Version of the Logo which has already been designed and linked as a file (first file). We want the entire back of the card to simply just be the black background logo. In terms of the front of the card, would like to see a smaller version of the white background logo (linked as the second file) in the top left hand corner - of course, feel free to get creative and we can make revisions together along the way! and Then after that, just text. We want the card to be sharp, clean, easy on the eyes and highly professional looking. We would like the card to include the Full name of the Company (Marlbeck Group of Companies), Name of the Person, Title, Phone, Email. If possible please provide the front part of the card for 3 people:

1) Marlbeck Group of Companies, Lena Okafor, Chief Financial Officer, 780-555-0162, lenaokafor@marlbeckgroup.example

2) Marlbeck Group of Companies, Tobias Okafor, Chief Executive Officer, 780-555-0148, tobiasokafor@marlbeckgroup.example

3) Marlbeck Group of Companies, Rui Dalton, Chief Operations Officer, 587-555-0193, ruidalton@marlbeckgroup.example

Thank you so much for considering our project & we look forward to seeing your designs!

```html
<!DOCTYPE html>
<html lang="en">
<head>
<meta charset="utf-8">
<title>Marlbeck – Executive Business Cards</title>
<link href="https://fonts.googleapis.com/css2?family=Lato:wght@400;700&family=Oswald:wght@600&display=swap" rel="stylesheet">
<style>
  :root {
    --stage: #1c1c1e;
    --card: #121212;
    --ink: #f4f7f8;
    --muted: #b9bcbe;
    --band: #ffffff;
    --rule: #8a8a8a;
  }
  * { margin: 0; padding: 0; box-sizing: border-box; }
  html, body {
    width: 1200px; height: 900px; overflow: hidden;
    background: var(--stage);
  }
  .stage {
    width: 1200px; height: 900px;
    display: grid;
    grid-template-columns: repeat(2, 560px);
    grid-template-rows: repeat(2, 320px);
    gap: 30px;
    justify-content: center;
    align-content: center;
  }
  .card {
    position: relative;
    width: 560px; height: 320px;
    background: var(--card);
    box-shadow: 0 12px 30px rgba(0,0,0,.55);
    overflow: hidden;
  }
  .card__band {
    position: absolute; left: 0; right: 0; bottom: 0;
    height: 12px; background: var(--band);
  }

  /* Logo side */
  .card--logo {
    display: flex; align-items: center; justify-content: center;
  }
  .wordmark {
    font-family: 'Lato', sans-serif;
    font-weight: 400;
    color: var(--ink);
    text-transform: uppercase;
  }
  .wordmark--large {
    font-size: 30px;
    letter-spacing: 12px;
    margin-right: -12px;
    margin-bottom: 12px;
  }

  /* Contact side */
  .card--contact {
    display: flex; align-items: center;
    padding: 0 28px 12px 28px;
  }
  .card__brand {
    position: absolute; top: 24px; left: 28px;
  }
  .wordmark--small {
    font-size: 15px;
    letter-spacing: 5px;
    display: block;
  }
  .company-name {
    font-family: 'Lato', sans-serif;
    font-weight: 400;
    font-size: 12px;
    color: var(--muted);
    margin-top: 5px;
    letter-spacing: .3px;
  }
  .identity {
    text-align: right;
    width: 180px;
    flex: none;
  }
  .identity__name {
    font-family: 'Oswald', sans-serif;
    font-weight: 600;
    font-size: 24px;
    letter-spacing: .5px;
    color: var(--ink);
    line-height: 1.1;
    text-transform: uppercase;
    white-space: nowrap;
  }
  .identity__title {
    font-family: 'Lato', sans-serif;
    font-weight: 400;
    font-size: 14px;
    color: var(--ink);
    margin-top: 2px;
    white-space: nowrap;
  }
  .divider {
    width: 1px; height: 76px;
    background: var(--rule);
    margin: 0 16px 0 20px;
    flex: none;
  }
  .contact-list { list-style: none; }
  .contact-list__item {
    display: flex; align-items: center; gap: 8px;
    font-family: 'Lato', sans-serif;
    font-size: 14px;
    color: var(--ink);
    line-height: 1.65;
    white-space: nowrap;
  }
  .contact-list__icon { width: 13px; height: 13px; flex: none; }
</style>
</head>
<body>
  <main class="stage">
    <section class="card card--logo">
      <span class="wordmark wordmark--large">Marlbeck</span>
      <div class="card__band"></div>
    </section>

    <section class="card card--contact">
      <div class="card__brand">
        <span class="wordmark wordmark--small">Marlbeck</span>
        <p class="company-name">Marlbeck Group of Companies</p>
      </div>
      <div class="identity">
        <h2 class="identity__name">Lena Okafor</h2>
        <p class="identity__title">Chief Financial Officer</p>
      </div>
      <div class="divider"></div>
      <ul class="contact-list">
        <li class="contact-list__item">
          <svg class="contact-list__icon" viewBox="0 0 24 24" fill="#f4f7f8" aria-hidden="true"><path d="M6.6 10.8a15.1 15.1 0 0 0 6.6 6.6l2.2-2.2c.3-.3.7-.4 1-.2 1.1.4 2.3.6 3.6.6.6 0 1 .4 1 1V20c0 .6-.4 1-1 1A17 17 0 0 1 3 4c0-.6.4-1 1-1h3.5c.6 0 1 .4 1 1 0 1.3.2 2.5.6 3.6.1.3 0 .7-.2 1z"/></svg>
          780-555-0162
        </li>
        <li class="contact-list__item">
          <svg class="contact-list__icon" viewBox="0 0 24 24" fill="#f4f7f8" aria-hidden="true"><path d="M2 5h20v14H2z M3.5 6.5 12 13l8.5-6.5" stroke="#121212" stroke-width="1.6"/></svg>
          lenaokafor@marlbeckgroup.example
        </li>
        <li class="contact-list__item">
          <svg class="contact-list__icon" viewBox="0 0 24 24" fill="none" stroke="#f4f7f8" stroke-width="1.8" aria-hidden="true"><circle cx="12" cy="12" r="9.5"/><ellipse cx="12" cy="12" rx="4" ry="9.5"/><path d="M2.5 12h19M4 7h16M4 17h16"/></svg>
          www.marlbeckgroup.example
        </li>
      </ul>
      <div class="card__band"></div>
    </section>

    <section class="card card--contact">
      <div class="card__brand">
        <span class="wordmark wordmark--small">Marlbeck</span>
        <p class="company-name">Marlbeck Group of Companies</p>
      </div>
      <div class="identity">
        <h2 class="identity__name">Tobias Okafor</h2>
        <p class="identity__title">Chief Executive Officer</p>
      </div>
      <div class="divider"></div>
      <ul class="contact-list">
        <li class="contact-list__item">
          <svg class="contact-list__icon" viewBox="0 0 24 24" fill="#f4f7f8" aria-hidden="true"><path d="M6.6 10.8a15.1 15.1 0 0 0 6.6 6.6l2.2-2.2c.3-.3.7-.4 1-.2 1.1.4 2.3.6 3.6.6.6 0 1 .4 1 1V20c0 .6-.4 1-1 1A17 17 0 0 1 3 4c0-.6.4-1 1-1h3.5c.6 0 1 .4 1 1 0 1.3.2 2.5.6 3.6.1.3 0 .7-.2 1z"/></svg>
          780-555-0148
        </li>
        <li class="contact-list__item">
          <svg class="contact-list__icon" viewBox="0 0 24 24" fill="#f4f7f8" aria-hidden="true"><path d="M2 5h20v14H2z M3.5 6.5 12 13l8.5-6.5" stroke="#121212" stroke-width="1.6"/></svg>
          tobiasokafor@marlbeckgroup.example
        </li>
        <li class="contact-list__item">
          <svg class="contact-list__icon" viewBox="0 0 24 24" fill="none" stroke="#f4f7f8" stroke-width="1.8" aria-hidden="true"><circle cx="12" cy="12" r="9.5"/><ellipse cx="12" cy="12" rx="4" ry="9.5"/><path d="M2.5 12h19M4 7h16M4 17h16"/></svg>
          www.marlbeckgroup.example
        </li>
      </ul>
      <div class="card__band"></div>
    </section>

    <section class="card card--contact">
      <div class="card__brand">
        <span class="wordmark wordmark--small">Marlbeck</span>
        <p class="company-name">Marlbeck Group of Companies</p>
      </div>
      <div class="identity">
        <h2 class="identity__name">Rui Dalton</h2>
        <p class="identity__title">Chief Operations Officer</p>
      </div>
      <div class="divider"></div>
      <ul class="contact-list">
        <li class="contact-list__item">
          <svg class="contact-list__icon" viewBox="0 0 24 24" fill="#f4f7f8" aria-hidden="true"><path d="M6.6 10.8a15.1 15.1 0 0 0 6.6 6.6l2.2-2.2c.3-.3.7-.4 1-.2 1.1.4 2.3.6 3.6.6.6 0 1 .4 1 1V20c0 .6-.4 1-1 1A17 17 0 0 1 3 4c0-.6.4-1 1-1h3.5c.6 0 1 .4 1 1 0 1.3.2 2.5.6 3.6.1.3 0 .7-.2 1z"/></svg>
          587-555-0193
        </li>
        <li class="contact-list__item">
          <svg class="contact-list__icon" viewBox="0 0 24 24" fill="#f4f7f8" aria-hidden="true"><path d="M2 5h20v14H2z M3.5 6.5 12 13l8.5-6.5" stroke="#121212" stroke-width="1.6"/></svg>
          ruidalton@marlbeckgroup.example
        </li>
        <li class="contact-list__item">
          <svg class="contact-list__icon" viewBox="0 0 24 24" fill="none" stroke="#f4f7f8" stroke-width="1.8" aria-hidden="true"><circle cx="12" cy="12" r="9.5"/><ellipse cx="12" cy="12" rx="4" ry="9.5"/><path d="M2.5 12h19M4 7h16M4 17h16"/></svg>
          www.marlbeckgroup.example
        </li>
      </ul>
      <div class="card__band"></div>
    </section>
  </main>
</body>
</html>
```